Create an Engaging Yet Simple Cycle Infographic to be featured in new book

I require a clearly designed, simple to navigate infographic. It will depict a "CYCLE-style" Framework that includes 7-stages which are underpinned by 6-enablers. The cycle is the core concept of a new business book. Each component also needs a simple graphic/ icon that can be used as a short-cut to identify the specific stage or enabler. The attached brief provides further details.

Target Market(s)

Business leaders

Font styles to use
Serif

Colors
000000

Requirements
Must have
• Simple, easy to engage with, fit on portrait-oriented book page

```html
<!DOCTYPE html>
<html lang="en">
<head>
<meta charset="utf-8">
<title>The Orbit Framework</title>
<link rel="stylesheet" href="https://fonts.googleapis.com/css2?family=Montserrat:wght@800&family=Roboto+Condensed:wght@400;700&display=swap">
<style>
  :root {
    --ink: #2b2b2b;
    --header: #353535;
    --green: #1f8a3a;
    --brown: #4a3528;
    --ring: #b9b2ad;
    --house: #b3aca8;
    --panel: #cfcac6;
    --label: #3a3a3a;
    --white: #ffffff;
  }
  html, body {
    margin: 0;
    padding: 0;
    width: 788px;
    height: 1200px;
    overflow: hidden;
    background: var(--white);
  }
  .canvas {
    position: relative;
    width: 788px;
    height: 1200px;
    overflow: hidden;
  }
  .title-band {
    position: absolute;
    left: 0; top: 0;
    width: 788px;
    height: 200px;
    background: var(--header);
    display: flex;
    align-items: center;
    justify-content: center;
  }
  .title-band h1 {
    margin: 0;
    color: var(--white);
    font-family: "Montserrat", sans-serif;
    font-weight: 800;
    font-size: 48px;
    letter-spacing: 0.5px;
  }
  .cycle-diagram {
    position: absolute;
    left: 0; top: 0;
  }
  .stage-label {
    font-family: "Roboto Condensed", sans-serif;
    font-weight: 700;
    font-size: 22px;
    fill: var(--label);
    text-anchor: middle;
  }
  .stage-box {
    fill: var(--ink);
    stroke: var(--green);
    stroke-width: 4;
  }
  .icon {
    fill: none;
    stroke: var(--white);
    stroke-width: 3;
    stroke-linecap: round;
    stroke-linejoin: round;
  }
  .icon-fill { fill: var(--white); stroke: none; }
  .enabler-panel {
    position: absolute;
    left: 52px; top: 862px;
    width: 684px;
    height: 172px;
    background: var(--panel);
    display: flex;
    justify-content: center;
    align-items: center;
    gap: 10px;
  }
  .enabler {
    width: 100px;
    height: 128px;
    background: var(--brown);
    display: flex;
    flex-direction: column;
    align-items: center;
    justify-content: flex-start;
    box-sizing: border-box;
    padding-top: 14px;
  }
  .enabler svg { width: 48px; height: 48px; }
  .enabler-name {
    margin-top: 10px;
    color: var(--white);
    font-family: "Roboto Condensed", sans-serif;
    font-weight: 400;
    font-size: 15px;
    line-height: 17px;
    text-align: center;
  }
</style>
</head>
<body>
<div class="canvas">
  <svg class="cycle-diagram" width="788" height="1200" viewBox="0 0 788 1200" aria-label="Seven-stage cycle">
    <path d="M132 744 A262 262 0 0 1 656 744 Z" fill="var(--brown)"/>
    <path d="M98 744 A296 296 0 0 1 690 744 L656 744 A262 262 0 0 0 132 744 Z" fill="var(--ring)"/>
    <polygon points="410,456 448,470 410,486" fill="var(--white)" opacity="0.85"/>
    <polygon points="618,640 656,640 636,676" fill="var(--white)" opacity="0.85"/>
    <path d="M68 744 A326 326 0 0 1 720 744 L690 744 A296 296 0 0 0 98 744 Z" fill="var(--green)"/>
    <g stroke="var(--white)" stroke-width="2.5">
      <line x1="108.1" y1="667.4" x2="79.1" y2="659.6"/>
      <line x1="184.7" y1="534.7" x2="163.5" y2="513.5"/>
      <line x1="317.4" y1="458.1" x2="309.6" y2="429.1"/>
      <line x1="470.6" y1="458.1" x2="478.4" y2="429.1"/>
      <line x1="603.3" y1="534.7" x2="624.5" y2="513.5"/>
      <line x1="679.9" y1="667.4" x2="708.9" y2="659.6"/>
    </g>
    <polygon points="250,862 250,690 394,560 538,690 538,862" fill="var(--house)"/>
    <g stroke="var(--green)" stroke-width="4" fill="var(--green)">
      <line x1="89" y1="780" x2="236" y2="780"/>
      <polygon points="248,780 232,772 232,788" stroke="none"/>
      <line x1="699" y1="780" x2="552" y2="780"/>
      <polygon points="540,780 556,772 556,788" stroke="none"/>
    </g>
    <g stroke="var(--green)" stroke-width="4">
      <line x1="111.7" y1="581" x2="82" y2="564"/>
      <line x1="231" y1="461.7" x2="214" y2="432"/>
      <line x1="394" y1="418" x2="394" y2="380"/>
      <line x1="557" y1="461.7" x2="574" y2="432"/>
      <line x1="676.3" y1="581" x2="706" y2="564"/>
    </g>

    <!-- SEE -->
    <rect class="stage-box" x="31" y="751" width="58" height="58"/>
    <text class="stage-label" x="56" y="838">SEE</text>
    <g class="icon" transform="translate(60 780)">
      <path d="M-9 4 A11 11 0 1 1 9 4 L5 9 L-5 9 Z"/>
      <line x1="-4" y1="13" x2="4" y2="13"/>
      <line x1="0" y1="-20" x2="0" y2="-17"/><line x1="-17" y1="-6" x2="-14" y2="-6"/><line x1="17" y1="-6" x2="14" y2="-6"/>
    </g>

    <!-- UNDERSTAND -->
    <text class="stage-label" x="72" y="515">UNDERSTAND</text>
    <rect class="stage-box" x="43" y="529" width="58" height="58"/>
    <g class="icon" transform="translate(72 562)">
      <path d="M-14 4 A14 14 0 0 1 14 4 Z"/>
      <line x1="-18" y1="8" x2="18" y2="8"/>
      <line x1="0" y1="-16" x2="0" y2="-13"/><line x1="-12" y1="-11" x2="-10" y2="-9"/><line x1="12" y1="-11" x2="10" y2="-9"/>
    </g>

    <!-- PRIORITISE -->
    <text class="stage-label" x="208" y="379">PRIORITISE</text>
    <rect class="stage-box" x="179" y="393" width="58" height="58"/>
    <g transform="translate(208 422)">
      <rect x="-15" y="-15" width="30" height="30" rx="3" class="icon-fill"/>
      <g stroke="var(--ink)" stroke-width="3"><line x1="-9" y1="-7" x2="9" y2="-7"/><line x1="-9" y1="0" x2="5" y2="0"/><line x1="-9" y1="7" x2="1" y2="7"/></g>
    </g>

    <!-- DESIGN -->
    <text class="stage-label" x="394" y="329">DESIGN</text>
    <rect class="stage-box" x="365" y="343" width="58" height="58"/>
    <g class="icon" transform="translate(394 372)">
      <rect x="-8" y="-14" width="22" height="16"/><rect x="-12" y="-9" width="22" height="16"/>
      <rect x="-16" y="-4" width="22" height="16" class="icon-fill"/>
    </g>

    <!-- PLAN -->
    <text class="stage-label" x="580" y="379">PLAN</text>
    <rect class="stage-box" x="551" y="393" width="58" height="58"/>
    <g class="icon" transform="translate(580 422)">
      <rect x="-11" y="-14" width="22" height="29"/>
      <line x1="-6" y1="-18" x2="-6" y2="-11"/><line x1="0" y1="-18" x2="0" y2="-11"/><line x1="6" y1="-18" x2="6" y2="-11"/>
      <line x1="-6" y1="-3" x2="6" y2="-3"/><line x1="-6" y1="3" x2="6" y2="3"/><line x1="-6" y1="9" x2="3" y2="9"/>
    </g>

    <!-- MOVE -->
    <text class="stage-label" x="716" y="515">MOVE</text>
    <rect class="stage-box" x="687" y="529" width="58" height="58"/>
    <g transform="translate(716 558)" class="icon-fill">
      <rect x="-14" y="6" width="5" height="9"/><rect x="-6" y="1" width="5" height="14"/><rect x="2" y="-5" width="5" height="20"/><rect x="10" y="-11" width="5" height="26"/>
      <path d="M-15 -2 L4 -15" stroke="var(--white)" stroke-width="2.5" fill="none"/>
      <polygon points="8,-18 -1,-16 4,-11"/>
    </g>

    <!-- LEARN -->
    <rect class="stage-box" x="699" y="751" width="58" height="58"/>
    <text class="stage-label" x="730" y="838">LEARN</text>
    <g class="icon" transform="translate(728 778)">
      <path d="M0 16 C-8 6 -12 0 -12 -4 A12 12 0 0 1 12 -4 C12 0 8 6 0 16 Z"/>
      <circle cx="0" cy="-4" r="4" class="icon-fill"/>
    </g>
  </svg>

  <header class="title-band">
    <h1>THE ORBIT FRAMEWORK</h1>
  </header>

  <section class="enabler-panel" aria-label="Six enablers">
    <div class="enabler">
      <svg viewBox="0 0 48 48"><circle cx="24" cy="24" r="21" class="icon"/><path class="icon" d="M15 22 A10 10 0 0 1 33 20 M33 26 A10 10 0 0 1 15 28"/><polygon class="icon-fill" points="34,14 35,22 28,20"/><polygon class="icon-fill" points="14,34 13,26 20,28"/></svg>
      <div class="enabler-name">Flexible Outlook</div>
    </div>
    <div class="enabler">
      <svg viewBox="0 0 48 48"><circle cx="24" cy="24" r="21" class="icon"/><circle cx="24" cy="20" r="9" class="icon-fill"/><line x1="24" y1="29" x2="24" y2="37" class="icon"/></svg>
      <div class="enabler-name">Steady Foundations</div>
    </div>
    <div class="enabler">
      <svg viewBox="0 0 48 48"><path class="icon" d="M16 4 L24 18 L32 4"/><circle cx="24" cy="30" r="12" class="icon"/><circle cx="24" cy="30" r="6" class="icon-fill"/></svg>
      <div class="enabler-name">The Clear Purpose</div>
    </div>
    <div class="enabler">
      <svg viewBox="0 0 48 48"><g class="icon-fill"><circle cx="24" cy="12" r="6"/><path d="M14 40 L14 26 A10 8 0 0 1 34 26 L34 40 Z"/><circle cx="9" cy="17" r="4"/><path d="M2 40 L2 30 A7 6 0 0 1 12 25 L12 40 Z"/><circle cx="39" cy="17" r="4"/><path d="M46 40 L46 30 A7 6 0 0 0 36 25 L36 40 Z"/></g></svg>
      <div class="enabler-name">Agile Guidance</div>
    </div>
    <div class="enabler">
      <svg viewBox="0 0 48 48"><g class="icon"><line x1="24" y1="6" x2="24" y2="40"/><line x1="8" y1="12" x2="40" y2="12"/><line x1="16" y1="42" x2="32" y2="42"/><path d="M8 12 L2 26 L14 26 Z"/><path d="M40 12 L34 26 L46 26 Z"/></g></svg>
      <div class="enabler-name">Healthy Network</div>
    </div>
    <div class="enabler">
      <svg viewBox="0 0 48 48"><g class="icon"><path d="M24 4 A20 20 0 1 1 6 16"/><polyline points="24,12 24,24 32,28"/></g><polygon class="icon-fill" points="2,10 12,12 6,20"/></svg>
      <div class="enabler-name">Lasting Resolve</div>
    </div>
  </section>
</div>
</body>
</html>
```